Maple Hollow - New monument signage for our apartment community

We have a monument sign that we would like to replace with a fresh, clean, and easy to read new design. I've included a couple pictures of the physical sign - people will be seeing this while driving very fast. It needs to be simple and easy to quickly see while driving.

* Maple Hollow
* Newly Renovated!
* www.maplehollowliving-example.com
* 555 - 318 - 7096

Suggestions:
* Bright colors
* Bold fonts
* Focus on phone number being easy to read

*** I attached a picture of something similar we did at one of our other apartment communities (Willowmere townhomes)

Logo Text

Maple Hollow Apartment Community

```html
<!DOCTYPE html>
<html lang="en">
<head>
<meta charset="utf-8">
<title>Maple Hollow Apartment Community – Monument Sign</title>
<link href="https://fonts.googleapis.com/css2?family=Montserrat:wght@700;800&display=swap" rel="stylesheet">
<style>
  :root {
    --page-bg: #ffffff;
    --sign-navy: #06345f;
    --sign-yellow: #f5f00f;
    --sign-white: #ffffff;
  }
  html, body {
    margin: 0;
    padding: 0;
    width: 1200px;
    height: 1200px;
    overflow: hidden;
    background: var(--page-bg);
    font-family: "Montserrat", Arial, sans-serif;
  }
  .canvas {
    position: relative;
    width: 1200px;
    height: 1200px;
  }
  .sign {
    position: absolute;
    left: 229px;
    top: 329px;
    width: 742px;
    height: 541px;
    background: var(--sign-navy);
    overflow: hidden;
  }
  .sign__ribbon {
    position: absolute;
    left: 0;
    top: 0;
    width: 742px;
    height: 541px;
  }
  .sign__text {
    position: absolute;
    right: 26px;
    text-align: right;
    font-weight: 800;
    white-space: nowrap;
    line-height: 1;
  }
  .sign__name {
    top: 112px;
    color: var(--sign-white);
    font-size: 78px;
    line-height: 86px;
    letter-spacing: 0;
  }
  .sign__apartment {
    top: 285px;
    color: var(--sign-yellow);
    font-size: 56px;
    letter-spacing: 23px;
    margin-right: -23px;
  }
  .sign__community {
    top: 352px;
    color: var(--sign-white);
    font-size: 31px;
    letter-spacing: 42px;
    margin-right: -42px;
  }
  .sign__web {
    top: 403px;
    color: var(--sign-white);
    font-size: 21px;
    letter-spacing: 2.2px;
    right: 40px;
  }
  .sign__web-domain { color: var(--sign-yellow); }
  .sign__phone {
    top: 450px;
    right: 36px;
    color: var(--sign-white);
    font-size: 68px;
    letter-spacing: 1px;
  }
</style>
</head>
<body>
<div class="canvas">
  <div class="sign">
    <svg class="sign__ribbon" viewBox="0 0 742 541" aria-hidden="true">
      <polygon points="0,95 440,0 0,210" fill="var(--sign-yellow)"/>
      <polygon points="0,95 440,0 0,210" fill="var(--sign-yellow)"/>
      <polygon points="0,95 170,0 440,0 0,210" fill="var(--sign-yellow)"/>
      <g transform="rotate(-24 150 110)" font-family="Montserrat, Arial, sans-serif" font-weight="800" fill="var(--sign-navy)" text-anchor="middle">
        <text x="175" y="92" font-size="34">NEWLY</text>
        <text x="160" y="130" font-size="34">RENOVATED !</text>
      </g>
    </svg>
    <div class="sign__text sign__name">MAPLE<br>HOLLOW</div>
    <div class="sign__text sign__apartment">APARTMENT</div>
    <div class="sign__text sign__community">COMMUNITY</div>
    <div class="sign__text sign__web">www.<span class="sign__web-domain">maplehollowliving-example</span>.com</div>
    <div class="sign__text sign__phone">555 - 318 - 7096</div>
  </div>
</div>
</body>
</html>
```